Newsletter Design Project

We need a template design for Mailchimp (html) newsletter (two types, one with only one property and one with several). One will be a b2b newsletter the other one a b2c.

It needs to work as a template in mailchimp and be branded like our website www.tide-vista-benalora.com

Reason: have not yet found the design that will be the one.

Target Market(s)

b2b: real estate agencies, b2c: real estate buyers in Spain in the middle and luxury segment: €350 k plus

Industry/Entity Type

Property

Requirements
Must have
• mailchimp compatible

```html
<!DOCTYPE html>
<html lang="en">
<head>
<meta charset="utf-8">
<title>Tide Vista Newsletter</title>
<link rel="stylesheet" href="https://fonts.googleapis.com/css2?family=Arimo:wght@400;700&display=swap">
<style>
  :root {
    --page-bg: #ececea;
    --frame: #cdbd6c;
    --panel: #ffffff;
    --ink: #2b2b2b;
    --muted: #555555;
    --rule: #d9cc8a;
    --button: #1c1c1c;
    --button-text: #ffffff;
    --footer-box: #e6e6e6;
    --caption-bg: rgba(180, 150, 60, 0.85);
  }
  * { box-sizing: border-box; margin: 0; padding: 0; }
  html, body { width: 800px; height: 1200px; overflow: hidden; }
  body {
    background: var(--page-bg);
    font-family: "Arimo", Arial, sans-serif;
    color: var(--ink);
    position: relative;
  }
  .preheader {
    height: 34px; background: #3a3a3a; color: #fff;
    font-size: 13px; text-align: center; line-height: 34px;
  }
  .preheader a { color: var(--frame); }
  .frame {
    position: absolute; left: 133px; top: 40px; width: 540px; height: 1060px;
    background: var(--frame); padding: 20px;
  }
  .panel { background: var(--panel); height: 100%; padding: 20px 22px 0; position: relative; }
  .masthead { display: flex; justify-content: space-between; align-items: flex-start; height: 92px; border-bottom: 3px solid var(--rule); }
  .brand { display: flex; align-items: center; gap: 10px; margin-top: 12px; }
  .brand-mark { width: 22px; height: 22px; background: var(--ink); }
  .brand-name { font-size: 26px; font-weight: 700; color: var(--ink); letter-spacing: 1px; }
  .contact { text-align: right; font-size: 14px; font-weight: 700; line-height: 18px; }
  .contact .call { font-size: 17px; display: flex; align-items: center; gap: 6px; justify-content: flex-end; }
  .contact .phone { color: #b3312b; font-weight: 400; }
  .section-title { font-size: 14px; font-weight: 700; margin: 14px 0 10px; }
  .photo { border-radius: 2px; position: relative; }
  .photo-hero { height: 160px; background: linear-gradient(160deg, #9bb7c6 0%, #caa97a 45%, #6a7e4a 100%); }
  .caption { position: absolute; left: 0; bottom: 14px; }
  .caption span { display: block; color: #fff; font-size: 12px; font-weight: 700; padding: 3px 10px; background: var(--caption-bg); margin-top: 2px; width: max-content; }
  .caption .price { background: rgba(40, 40, 40, 0.8); }
  .copy { font-size: 11.5px; line-height: 15px; color: var(--muted); margin-top: 12px; }
  .button {
    display: inline-block; background: var(--button); color: var(--button-text);
    font-size: 12px; padding: 9px 20px; border-radius: 3px; margin-top: 10px; text-decoration: none;
  }
  .divider { border: 0; border-top: 3px solid var(--rule); margin: 20px 0 0; }
  .previews { display: flex; gap: 20px; }
  .preview { flex: 1; }
  .photo-room { height: 144px; background: linear-gradient(180deg, #d8b98a 0%, #a57a4c 60%, #6e4a2c 100%); }
  .photo-interior { height: 144px; background: linear-gradient(180deg, #c89f70 0%, #8a5a38 55%, #4a3020 100%); }
  .subscribe {
    background: var(--footer-box); margin: 32px -22px 0; padding: 14px 22px;
    font-size: 11px; line-height: 15px; color: var(--muted);
  }
  .subscribe p + p { margin-top: 12px; }
  .subscribe a { color: var(--muted); }
  .legal { text-align: center; font-size: 10.5px; color: var(--muted); margin-top: 18px; }
</style>
</head>
<body>
  <div class="preheader">Email not displaying correctly? <a href="#">View it in your browser</a></div>
  <div class="frame">
    <div class="panel">
      <header class="masthead">
        <div class="brand"><span class="brand-mark"></span><span class="brand-name">TIDE VISTA</span></div>
        <div class="contact">
          <div class="call">
            <svg width="16" height="16" viewBox="0 0 24 24" aria-hidden="true"><path fill="#2b2b2b" d="M6.6 10.8a15.1 15.1 0 0 0 6.6 6.6l2.2-2.2c.3-.3.7-.4 1-.2 1.1.4 2.3.6 3.6.6.6 0 1 .4 1 1V20c0 .6-.4 1-1 1A17 17 0 0 1 3 4c0-.6.4-1 1-1h3.5c.6 0 1 .4 1 1 0 1.3.2 2.5.6 3.6.1.3 0 .7-.2 1z"/></svg>
            CALL US
          </div>
          <div class="phone">951470263</div>
          <div class="phone">612384907</div>
        </div>
      </header>

      <h2 class="section-title">Title For 1 Large Image</h2>
      <div class="photo photo-hero" role="img" aria-label="Villa exterior with pool and garden terrace">
        <div class="caption"><span>Villa for Sale in Marbella</span><span class="price">Price : 650,000 €</span></div>
      </div>
      <p class="copy">A ready to move in to charming 5 bedroom villa in Marbella. The house is built on a well located plot of close to 900 m2 in Marbella, only a short stroll from the sea.<br>The property has a private pool in a nicely kept garden. Inside one finds an ample living room and a large kitchen on the ground floor. Furthermore on the groundfloor 4 bedrooms.<br>The upper floor is dedicated to a large master bedroom with en suite bathroom.</p>
      <a class="button" href="#">More info &gt;&gt;</a>

      <hr class="divider">
      <h2 class="section-title">Another Preview</h2>
      <div class="previews">
        <article class="preview">
          <div class="photo photo-room" role="img" aria-label="Bright bedroom with double bed"></div>
          <p class="copy">A ready to move in to charming 5 bedroom villa in Marbella. The house is built on a well located plot of close to 900 m2 in Marbella, only a short stroll from the sea. The property has a private pool in a nicely</p>
          <a class="button" href="#">More info &gt;&gt;</a>
        </article>
        <article class="preview">
          <div class="photo photo-interior" role="img" aria-label="Rustic interior with wooden beams and archway"></div>
          <p class="copy">A ready to move in to charming 5 bedroom villa in Marbella. The house is built on a well located plot of close to 900 m2 in Marbella, only a short stroll from the sea. The property has a private pool in a nicely</p>
          <a class="button" href="#">More info &gt;&gt;</a>
        </article>
      </div>

      <footer>
        <div class="subscribe">
          <p>You are receiving this email because you subscribe to our mailing list for updates about our Product. You may have opted in at our website (www.tide-vista-benalora.com)</p>
          <p>If you don't want to receive emails anymore - <a href="#">Unsubscribe</a></p>
        </div>
        <p class="legal">© TideVista All Right Reserved</p>
      </footer>
    </div>
  </div>
</body>
</html>
```